'Orla Property Development' Business Card

Business Card Features:

High Quality (potentially textured) thick card - preference is white textured card

Logo (supplied)

We plan to use the vertical logo as the main logo. But i am happy for people to use either if they find it works better for the design of the card.

The building icon and also the insert to the 'E' is in a metallic finish, i think this should be finished in a metallic embossed or raised style.
Updates

Please note i have attached both a horizontal and Vertical Logo for your reference. We plan to use the vertical logo as the main logo. But i am happy for people to use either if they find it works better for the design of the card.

Please note i am considering having the cards made on stainless steel. This introduces the option of having cut outs in the card and etching or printing for the design. If you have a good concept for this please submit.

http://www.quorvantprint.co.uk/black-metal-cards# this is a site that makes the metal cards to offer some direction . . . . Please note i am basic the selection o the best design, if that means normal print cards on paper then this is what i will choose. But there are some great options with the metal. Thanks.

Industry/Entity Type

Building

Requirements
Must have
• Helvetica font to details side of card - logo as supplied to opposite side.

Card Details:

Darren Ashcombe
Managing Director

+61 438 615 207
+61 3 8276 4139

PO Box 73
Bentleigh, VIC 3024

darren@orla.properties

www.orla.properties

```html
<!DOCTYPE html>
<html lang="en">
<head>
<meta charset="utf-8">
<title>Orla Property Development – Business Card</title>
<link href="https://fonts.googleapis.com/css2?family=Arimo:wght@400;700&display=swap" rel="stylesheet">
<style>
  :root {
    --backdrop: #e9e7e3;
    --card-stock: #a8a8a8;
    --card-shadow: rgba(0, 0, 0, 0.22);
    --brand-ink: #4b4b4d;
    --detail-ink: #ffffff;
    --divider: #ffffff;
  }
  * { margin: 0; padding: 0; box-sizing: border-box; }
  html, body {
    width: 1200px;
    height: 800px;
    overflow: hidden;
    background: var(--backdrop);
    font-family: "Arimo", "Helvetica Neue", Helvetica, Arial, sans-serif;
  }
  .canvas {
    position: relative;
    width: 1200px;
    height: 800px;
  }
  .card {
    position: absolute;
    top: 255px;
    width: 520px;
    height: 290px;
    background: var(--card-stock);
    box-shadow: 0 10px 28px var(--card-shadow);
  }
  .card--front { left: 60px; }
  .card--back  { left: 620px; }

  /* Front: centred brand name */
  .brand {
    color: var(--brand-ink);
    font-weight: 700;
    display: flex;
    align-items: center;
  }
  .brand__mark {
    background: var(--brand-ink);
  }
  .brand__words { display: flex; flex-direction: column; }
  .brand__name { line-height: 1; letter-spacing: 0.04em; }
  .brand__tagline { line-height: 1.2; letter-spacing: 0.03em; }

  .card--front .brand {
    position: absolute;
    left: 50%;
    top: 50%;
    transform: translate(-50%, -50%);
    gap: 16px;
  }
  .card--front .brand__mark { width: 34px; height: 34px; }
  .card--front .brand__name { font-size: 64px; }
  .card--front .brand__tagline { font-size: 15px; margin-top: 4px; }

  /* Back: brand left, divider, details right */
  .card--back .brand {
    position: absolute;
    left: 40px;
    top: 140px;
    gap: 12px;
  }
  .card--back .brand__mark { width: 20px; height: 20px; }
  .card--back .brand__name { font-size: 36px; }
  .card--back .brand__tagline { font-size: 9px; margin-top: 3px; }

  .card__divider {
    position: absolute;
    left: 268px;
    top: 28px;
    width: 3px;
    height: 234px;
    background: var(--divider);
  }
  .details {
    position: absolute;
    left: 296px;
    top: 62px;
    color: var(--detail-ink);
  }
  .details__name {
    font-size: 22px;
    font-weight: 700;
    line-height: 1.1;
  }
  .details__role {
    font-size: 16px;
    font-weight: 400;
    line-height: 1.2;
  }
  .details__contact {
    margin-top: 34px;
    list-style: none;
    font-size: 11px;
    font-weight: 700;
    line-height: 1.35;
  }
</style>
</head>
<body>
  <main class="canvas">
    <section class="card card--front" aria-label="Business card front">
      <div class="brand">
        <span class="brand__mark"></span>
        <div class="brand__words">
          <span class="brand__name">ORLA</span>
          <span class="brand__tagline">Property Development</span>
        </div>
      </div>
    </section>

    <section class="card card--back" aria-label="Business card back">
      <div class="brand">
        <span class="brand__mark"></span>
        <div class="brand__words">
          <span class="brand__name">ORLA</span>
          <span class="brand__tagline">Property Development</span>
        </div>
      </div>
      <div class="card__divider"></div>
      <div class="details">
        <p class="details__name">Darren Ashcombe</p>
        <p class="details__role">Managing Director</p>
        <ul class="details__contact">
          <li>0438615207</li>
          <li>1800 274 915</li>
          <li>PO BOX 73 Bentleigh, VIC 3024</li>
          <li>darren@orla.properties</li>
          <li>www.orla.properties</li>
        </ul>
      </div>
    </section>
  </main>
</body>
</html>
```